Hal's Remedies Business Card Design Project

I need a business card designed for my pharmacy Hal's Remedies. I would like just the logo on one side, maybe with black background and white lettering. The other side I would also like to include my logo which is attached. Also, please include my name and the following information:
Hal Norwick Owner/Pharm D.
Business address is 7163 N Birch Rd Sioux Falls, SD 57291.
Phone number is 605-318-6027 and fax # is 605-318-6031.
my email address is hal@halsremedies.example.
My website is www.halsremedies.example.
My business hours are Monday-Friday 8am-7 pm. Saturday 8am-12 pm. Sunday Closed.
I would like the design to include my logo colors, black, white, and neon green. Silver may be added as a highlight. Thanks.
Pharmacy
See above in product description

```html
<!DOCTYPE html>
<html lang="en">
<head>
<meta charset="utf-8">
<title>Hal's Remedies – Business Card</title>
<link rel="stylesheet" href="https://fonts.googleapis.com/css2?family=Montserrat:wght@400;500;600;700&display=swap">
<style>
  :root {
    --ink: #0b0b0b;
    --paper: #ffffff;
    --neon: #a6f20f;
    --stage: #e8ecf2;
    --stage-light: #f7f8fb;
    --text: #161616;
    --rule: #bcbcbc;
  }
  * { margin: 0; padding: 0; box-sizing: border-box; }
  html, body { width: 1200px; height: 900px; overflow: hidden; background: var(--paper); }
  body { font-family: "Montserrat", sans-serif; color: var(--text); position: relative; }

  .presentation {
    position: absolute; left: 33px; top: 37px; width: 1137px; height: 833px;
    background: radial-gradient(ellipse at 50% 45%, var(--stage-light) 0%, var(--stage) 75%);
  }

  .card {
    position: absolute; left: 321px; width: 515px; height: 316px;
    overflow: hidden;
    box-shadow: 0 2px 5px rgba(0,0,0,0.18);
  }
  .card--front { top: 110px; background: var(--ink); }
  .card--back { top: 482px; background: var(--paper); }

  .card__band {
    position: absolute; left: 0; right: 0; bottom: 0; background: var(--neon);
  }
  .card--front .card__band { height: 35px; }
  .card--back .card__band { height: 32px; display: flex; align-items: center; padding-left: 21px; }

  .hours { color: var(--paper); font-weight: 700; font-size: 13.5px; letter-spacing: 0.2px; }

  .brand { position: absolute; display: flex; align-items: center; }
  .brand__dot { border-radius: 50%; background: var(--neon); flex: none; }
  .brand__rule { flex: none; }
  .brand__name { font-weight: 600; letter-spacing: -0.6px; white-space: nowrap; }

  .card--front .brand { left: 36px; top: 113px; height: 72px; }
  .card--front .brand__dot { width: 44px; height: 44px; margin-right: 24px; }
  .card--front .brand__rule { width: 2px; height: 72px; background: var(--paper); margin-right: 20px; }
  .card--front .brand__name { color: var(--paper); font-size: 36px; }

  .card--back .brand { right: 24px; top: 16px; height: 44px; }
  .card--back .brand__dot { width: 30px; height: 30px; margin-right: 17px; }
  .card--back .brand__rule { width: 2px; height: 44px; background: var(--ink); margin-right: 12px; }
  .card--back .brand__name { color: var(--ink); font-size: 27px; }

  .address {
    position: absolute; right: 24px; top: 70px; text-align: right;
    font-size: 13px; line-height: 17px; font-weight: 500;
  }

  .person { position: absolute; left: 21px; top: 120px; }
  .person__name { font-size: 21px; font-weight: 700; letter-spacing: 0.2px; }
  .person__title { font-size: 14px; margin-top: 2px; }

  .contact { position: absolute; left: 21px; top: 188px; border-collapse: collapse; font-size: 13px; }
  .contact th { text-align: left; font-weight: 500; color: var(--neon); width: 75px; padding: 0; height: 20px; }
  .contact td { padding: 0; font-weight: 500; }
</style>
</head>
<body>
  <main class="presentation">
  </main>

  <section class="card card--front" aria-label="Card front">
    <div class="brand">
      <span class="brand__dot"></span>
      <span class="brand__rule"></span>
      <span class="brand__name">Hal's Remedies</span>
    </div>
    <div class="card__band"></div>
  </section>

  <section class="card card--back" aria-label="Card back">
    <div class="brand">
      <span class="brand__dot"></span>
      <span class="brand__rule"></span>
      <span class="brand__name">Hal's Remedies</span>
    </div>
    <p class="address">7163 N Birch Rd Sioux Falls<br>SD 57291</p>

    <div class="person">
      <p class="person__name">Hal Norwick</p>
      <p class="person__title">Owner/Pharm D.</p>
    </div>

    <table class="contact">
      <tr><th>tel</th><td>605-318-6027</td></tr>
      <tr><th>fax</th><td>605-318-6031</td></tr>
      <tr><th>email</th><td>hal@halsremedies.example</td></tr>
      <tr><th>website</th><td>www.halsremedies.example</td></tr>
    </table>

    <div class="card__band">
      <p class="hours">Monday-Friday 8am-7 pm. Saturday 8am-12 pm. Sunday Closed.</p>
    </div>
  </section>
</body>
</html>
```